Redesign Website - Current one too plain

The description is in the uploaded file. Please let me know if you need any more information. I'd prefer it if someone could implement the design to a WordPress site but the best design will win, regardless.
I would like the forms to look nice as well
UPDATE:
I don't think we can use the images that I provided, I think they make the site look a bit 'cheap' and I really don't know how to replace them. One thought I have had is to make the "Simple, Unique, Effective" a second feature on the right side of the page with the search on the left
Target Market(s)
Small companies, private sellers of cars and people who rent their caravan/holiday home out
Industry/Entity Type
Advertising
Number of Pages Required
3 page
Colors
Designer to choose colors to be used in the design.
Look and feel

```html
<!DOCTYPE html>
<html lang="en">
<head>
<meta charset="utf-8">
<title>Vanto – Simple advertising codes</title>
<link rel="stylesheet" href="https://fonts.googleapis.com/css2?family=Open+Sans:wght@300;400;600;700&family=Arimo:wght@700&display=swap">
<style>
  :root {
    --ink: #17303d;
    --ink-soft: #3b4a52;
    --muted: #8a8f93;
    --chevron: #a3a3a3;
    --paper: #f7f7f7;
    --white: #ffffff;
    --lime: #e2ff00;
    --logo-lime: #d9f20a;
    --accent-green: #2fcf8a;
    --blob-blue: #2150e0;
    --blob-teal: #0aa890;
    --blob-purple: #b08cf0;
    --blob-green: #8fec9e;
    --van-light: #d4d4d4;
    --van-dark: #8e8e8e;
  }
  * { box-sizing: border-box; margin: 0; padding: 0; }
  html, body { width: 1200px; height: 675px; overflow: hidden; background: var(--paper); }
  body { font-family: "Open Sans", "Segoe UI", sans-serif; color: var(--ink); }

  .page {
    position: relative;
    width: 1200px;
    height: 675px;
    overflow: hidden;
    background-color: var(--paper);
    background-image: radial-gradient(circle, rgba(0,0,0,0.05) 1px, transparent 1.2px);
    background-size: 22px 22px;
  }

  .glow { position: absolute; border-radius: 50%; filter: blur(40px); }
  .glow--blue   { left: -80px; top: -90px; width: 300px; height: 240px; background: var(--blob-blue); opacity: .95; }
  .glow--purple { left: 150px; top: -90px; width: 260px; height: 260px; background: var(--blob-purple); opacity: .9; }
  .glow--teal   { left: -90px; top: 40px;  width: 260px; height: 200px; background: var(--blob-teal); opacity: .9; }
  .glow--green  { left: -110px; top: 190px; width: 320px; height: 210px; background: var(--blob-green); opacity: .85; }

  .brand {
    position: absolute; left: 127px; top: 22px;
    display: flex; align-items: center; gap: 7px;
    color: var(--logo-lime);
    font-size: 21px; font-weight: 400; letter-spacing: 2px;
  }
  .brand__mark { width: 16px; height: 16px; border-radius: 50%; background: var(--logo-lime); }

  .nav { position: absolute; top: 33px; left: 0; width: 100%; }
  .nav a {
    position: absolute; color: var(--ink);
    font-size: 14px; font-weight: 600; text-decoration: none;
  }

  .hero-copy { position: absolute; left: 122px; top: 220px; }
  .hero-copy__title { font-size: 37px; font-weight: 700; line-height: 1.1; color: var(--ink); }
  .hero-copy__title::after {
    content: ""; display: inline-block; width: 8px; height: 8px; margin-left: 8px;
    border-radius: 50%; background: var(--accent-green);
  }
  .hero-copy__lead { margin-top: 8px; font-size: 13px; font-weight: 400; color: var(--ink-soft); }

  .van-visual {
    position: absolute; left: 97px; top: 369px; width: 426px; height: 202px;
    border-radius: 60px 90px 24px 24px;
    background: linear-gradient(180deg, var(--van-light), var(--van-dark));
  }

  .code-picker { position: absolute; left: 740px; top: 150px; width: 310px; }
  .code-picker__slot { position: absolute; top: 0; width: 150px; text-align: center; }
  .code-picker__slot--letter { left: 14px; }
  .code-picker__slot--number { left: 145px; }
  .code-picker__chevron { display: block; margin: 0 auto; }
  .code-picker__char {
    display: block; margin: 20px 0 26px;
    font-family: "Arimo", Arial, sans-serif; font-weight: 700;
    font-size: 184px; line-height: 150px; color: var(--ink);
  }

  .business-select { position: absolute; left: 736px; top: 449px; width: 296px; text-align: center; }
  .business-select__label { font-size: 11px; font-weight: 300; color: var(--ink-soft); }
  .business-select__options { margin-top: 14px; display: flex; justify-content: space-between; }
  .business-select__option {
    height: 32px; padding: 0 24px; border: none; border-radius: 6px;
    background: var(--white); color: var(--ink);
    font-family: inherit; font-size: 13px; font-weight: 400;
  }
  .business-select__option--car { width: 70px; padding: 0; }
  .business-select__option--caravan { width: 108px; padding: 0; }
  .business-select__option--company { width: 97px; padding: 0; }

  .search-button {
    position: absolute; left: 830px; top: 543px; width: 108px; height: 40px;
    border: none; border-radius: 5px; background: var(--lime);
    color: var(--ink); font-family: inherit; font-size: 14px; font-weight: 700;
  }

  .site-footer {
    position: absolute; left: 0; top: 640px; width: 100%; text-align: center;
    font-size: 12px; color: var(--ink-soft);
  }
</style>
</head>
<body>
<div class="page">
  <div class="glow glow--purple"></div>
  <div class="glow glow--blue"></div>
  <div class="glow glow--teal"></div>
  <div class="glow glow--green"></div>

  <div class="brand"><span class="brand__mark"></span><span>VANTO</span></div>

  <nav class="nav">
    <a href="#" style="left:674px">Home</a>
    <a href="#" style="left:753px">Advertise</a>
    <a href="#" style="left:852px">Contact</a>
    <a href="#" style="left:941px">Register</a>
    <a href="#" style="left:1032px">Login</a>
  </nav>

  <section class="hero-copy">
    <h1 class="hero-copy__title">Simple</h1>
    <p class="hero-copy__lead">Create your advert and display your code</p>
  </section>

  <div class="van-visual" role="img" aria-label="Photo of a silver van with a business name and an A1 code panel on its side"></div>

  <div class="code-picker">
    <div class="code-picker__slot code-picker__slot--letter">
      <svg class="code-picker__chevron" width="30" height="16" viewBox="0 0 30 16"><path d="M3 14 L15 3 L27 14" fill="none" stroke="var(--chevron)" stroke-width="4"/></svg>
      <span class="code-picker__char">A</span>
      <svg class="code-picker__chevron" width="30" height="16" viewBox="0 0 30 16"><path d="M3 2 L15 13 L27 2" fill="none" stroke="var(--chevron)" stroke-width="4"/></svg>
    </div>
    <div class="code-picker__slot code-picker__slot--number">
      <svg class="code-picker__chevron" width="30" height="16" viewBox="0 0 30 16"><path d="M3 14 L15 3 L27 14" fill="none" stroke="var(--chevron)" stroke-width="4"/></svg>
      <span class="code-picker__char">1</span>
      <svg class="code-picker__chevron" width="30" height="16" viewBox="0 0 30 16"><path d="M3 2 L15 13 L27 2" fill="none" stroke="var(--chevron)" stroke-width="4"/></svg>
    </div>
  </div>

  <div class="business-select">
    <p class="business-select__label">Select the line of business</p>
    <div class="business-select__options">
      <button class="business-select__option business-select__option--car">Car</button>
      <button class="business-select__option business-select__option--caravan">Caravan</button>
      <button class="business-select__option business-select__option--company">Company</button>
    </div>
  </div>

  <button class="search-button">Search</button>

  <footer class="site-footer">vanto.com</footer>
</div>
</body>
</html>
```